The Verdant Ledger App - Modernization & Graphics User Interface Friendliness Updates

We are Verdant Ledger, and we want to bring a new branding look and graphical user interface to the Verdant Ledger App. The app is a quick reference encyclopedia for all things produce. Boasting articles on over 2,000 produce items, with information ranging from taste and application to geographical and cultural significance. Included in its features are over 10 thousand recipes, and the Verdant Ledger App Harvest Circle – a global initiative to connect farmer, customer, and chef in one sustainable and easy to use application. The design needs to bring a greater sense of social connection – encouraging the user to participate in the 'Harvest Circled' experience voluntarily. The design should reflect a sense of authority reflecting the authenticity and reliability of the provided information, it's writing, and its sources. Download the App here: vledgr.example/install

Target Market(s)

Women and Men between ages 21-55.

Industry/Entity Type

Education

Font styles to use
Serif
Sans Serif

Colors

Designer to choose colors to be used in the design.

Requirements
Must have
• An updated user interface, the intuitive usability of the app is currently non-existent. We are looking to reflect as the authority on produce. The app design must reflect a professional, user-friendly, up-to-date, and trustworthy feel.
Nice to have
• To incorporate the social draw of the Harvest Circle we would like to include on the home page "Social Bubbles" (think Pictoloop stories) which updates with shared photos of produce and their location.
Should not have
• An overly complicated theme, distracting or unprofessional colors, and images.

```html
<!DOCTYPE html>
<html lang="en">
<head>
<meta charset="utf-8">
<title>Verdant Ledger App – Screens</title>
<link rel="stylesheet" href="https://fonts.googleapis.com/css2?family=Playfair+Display:wght@400;700;900&family=Montserrat:wght@400;500;600;700&display=swap">
<style>
  :root {
    --bg: #e8e2d8;
    --bg-light: #f1ede6;
    --screen: #ffffff;
    --ink: #111111;
    --ink-soft: #555555;
    --rule: #dddddd;
    --tab-bg: #f7f7f7;
    --icon: #b9b9b9;
    --icon-active: #4a4a4a;
    --badge: #f04b4b;
    --white: #ffffff;
  }
  * { box-sizing: border-box; margin: 0; padding: 0; }
  html, body { width: 1200px; height: 1025px; overflow: hidden; }
  body {
    background: radial-gradient(ellipse at 50% 45%, var(--bg-light) 0%, var(--bg) 70%);
    font-family: "Montserrat", sans-serif;
    color: var(--ink);
    position: relative;
  }
  .screen {
    position: absolute;
    top: 174px;
    width: 358px;
    height: 634px;
    overflow: hidden;
    background: var(--screen);
    box-shadow: 0 10px 30px rgba(80, 60, 30, 0.18);
  }
  .screen--detail { left: 160px; }
  .screen--feature { left: 681px; }

  /* Detail screen */
  .status-bar {
    position: absolute; top: 7px; left: 12px; right: 12px;
    display: flex; justify-content: space-between; align-items: center;
    font-size: 11px; font-weight: 500; color: var(--ink);
  }
  .status-bar__left, .status-bar__right { display: flex; align-items: center; gap: 4px; width: 110px; }
  .status-bar__right { justify-content: flex-end; }
  .signal { display: flex; gap: 2px; }
  .signal i { width: 5px; height: 5px; border-radius: 50%; background: var(--ink); display: block; }
  .signal i.off { background: none; border: 1px solid var(--ink); }
  .battery { width: 24px; height: 10px; border: 1px solid var(--ink); border-radius: 2px; padding: 1px; }
  .battery span { display: block; width: 100%; height: 100%; background: var(--ink); }

  .nav-bar {
    position: absolute; top: 36px; left: 0; right: 0; height: 22px;
    display: flex; align-items: center; justify-content: space-between;
    padding: 0 26px 0 26px;
  }
  .nav-bar__title { font-size: 12px; font-weight: 600; letter-spacing: -0.1px; }

  .produce-title {
    position: absolute; top: 88px; left: 27px;
    font-family: "Playfair Display", serif; font-weight: 900;
    font-size: 33px; letter-spacing: -0.8px;
  }
  .produce-photo {
    position: absolute; top: 160px; left: 60px; width: 240px; height: 162px;
    border-radius: 50% 50% 45% 45%;
    background: radial-gradient(ellipse at 60% 45%, #c9a448 0%, #d9683f 45%, #f2c13a 70%, rgba(255,255,255,0) 72%);
  }
  .section-label {
    position: absolute; top: 368px; left: 32px;
    font-size: 9px; font-weight: 700; letter-spacing: 0.1px;
  }
  .section-rule {
    position: absolute; top: 395px; left: 32px; width: 296px; height: 1px; background: var(--rule);
  }
  .section-body {
    position: absolute; top: 418px; left: 33px; width: 296px;
    font-size: 8.6px; line-height: 10.8px; letter-spacing: 0.5px; color: var(--ink-soft);
  }
  .section-body p + p { margin-top: 10px; }

  .tab-bar {
    position: absolute; left: 0; right: 0; bottom: 0; height: 50px;
    background: var(--tab-bg); border-top: 1px solid #efefef;
  }
  .tab-bar svg { position: absolute; top: 11px; }
  .tab-badge {
    position: absolute; top: 9px; left: 259px; width: 14px; height: 14px; border-radius: 50%;
    background: var(--badge); color: var(--white); font-size: 8px; font-weight: 600;
    display: flex; align-items: center; justify-content: center;
  }

  /* Feature screen */
  .feature-photo {
    position: absolute; inset: 0;
    background:
      radial-gradient(ellipse at 20% 40%, rgba(240,190,40,0.85) 0%, rgba(240,190,40,0) 25%),
      radial-gradient(ellipse at 90% 88%, rgba(232,180,30,0.8) 0%, rgba(232,180,30,0) 20%),
      radial-gradient(ellipse at 62% 50%, #c57a2a 0%, #9b5a2c 35%, rgba(155,90,44,0) 60%),
      linear-gradient(160deg, #ece9e2 0%, #cfcac0 40%, #a89a86 100%);
  }
  .feature-shade {
    position: absolute; inset: 0;
    background: linear-gradient(90deg, rgba(0,0,0,0.42) 0%, rgba(0,0,0,0.15) 70%, rgba(0,0,0,0) 100%);
  }
  .feature-kicker {
    position: absolute; top: 300px; left: 25px;
    font-family: "Playfair Display", serif; font-size: 15px; color: rgba(255,255,255,0.85);
  }
  .feature-title {
    position: absolute; top: 330px; left: 25px; width: 320px;
    font-family: "Playfair Display", serif; font-weight: 900;
    font-size: 31px; line-height: 37px; letter-spacing: -0.6px; color: var(--white);
  }
  .feature-button {
    position: absolute; top: 464px; left: 25px; width: 90px; height: 21px;
    border-radius: 11px; background: var(--white); color: var(--ink);
    font-size: 8px; font-weight: 700; letter-spacing: 1.2px;
    display: flex; align-items: center; justify-content: center;
  }
</style>
</head>
<body>

<section class="screen screen--detail" aria-label="Produce detail screen">
  <div class="status-bar">
    <div class="status-bar__left">
      <span class="signal"><i></i><i></i><i></i><i class="off"></i><i class="off"></i></span>
      <span>LUMA</span>
      <svg width="12" height="9" viewBox="0 0 12 9"><path d="M1 3.5a7 7 0 0 1 10 0M3 5.5a4 4 0 0 1 6 0" fill="none" stroke="#111" stroke-width="1.4" stroke-linecap="round"/><circle cx="6" cy="7.6" r="1.1" fill="#111"/></svg>
    </div>
    <span>4:21 PM</span>
    <div class="status-bar__right">
      <svg width="7" height="11" viewBox="0 0 7 11"><path d="M1 3l5 5-2.5 2V1L6 3 1 8" fill="none" stroke="#777" stroke-width="1"/></svg>
      <span>100%</span>
      <span class="battery"><span></span></span>
    </div>
  </div>

  <header class="nav-bar">
    <svg width="22" height="14" viewBox="0 0 22 14"><path d="M21 7H2M8 1L2 7l6 6" fill="none" stroke="#111" stroke-width="1.6" stroke-linecap="round" stroke-linejoin="round"/></svg>
    <span class="nav-bar__title">Fruit Produce</span>
    <svg width="17" height="14" viewBox="0 0 17 14"><path d="M0 2h17M0 7h17M0 12h17" stroke="#111" stroke-width="2.2"/></svg>
  </header>

  <h1 class="produce-title">Mangoes</h1>
  <div class="produce-photo" role="img" aria-label="Photo of two whole red-yellow mangoes with cut slices and a leaf"></div>

  <h2 class="section-label">DESCRIPTION &amp; TASTE</h2>
  <div class="section-rule"></div>
  <div class="section-body">
    <p>Each mango variety is listed with its season, origin and grower notes. Ripe fruit gives slightly to gentle pressure.</p>
    <p>The flesh is sweet and floral, with notes of peach, citrus and honey. Fibre varies by cultivar; some are smooth as custard while others stay firm and tangy. Choose fruit that smells fragrant at the stem end and store it at room temperature.</p>
  </div>

  <nav class="tab-bar" aria-label="Main tabs">
    <svg style="left:31px" width="24" height="26" viewBox="0 0 24 26"><path d="M12 3c1-2 3-3 5-3-1 2-3 3-5 3z" fill="#4a4a4a"/><circle cx="12" cy="15" r="10" fill="#4a4a4a"/></svg>
    <svg style="left:101px" width="20" height="26" viewBox="0 0 20 26"><rect x="1" y="1" width="18" height="24" fill="#e4e4e4" stroke="#b9b9b9"/><path d="M6 8l8 10M14 8L6 18" stroke="#b9b9b9" stroke-width="1.6"/></svg>
    <svg style="left:164px" width="32" height="24" viewBox="0 0 32 24"><path d="M2 12C8 3 24 3 30 12 24 21 8 21 2 12z" fill="none" stroke="#b9b9b9" stroke-width="2"/><circle cx="16" cy="12" r="5" fill="#b9b9b9"/></svg>
    <svg style="left:241px" width="28" height="24" viewBox="0 0 28 24"><rect x="1" y="3" width="26" height="20" fill="#e4e4e4" stroke="#b9b9b9"/><path d="M2 22l8-9 6 6 4-4 7 7z" fill="#b9b9b9"/></svg>
    <div class="tab-badge">7</div>
    <svg style="left:309px" width="24" height="24" viewBox="0 0 24 24"><circle cx="12" cy="12" r="8" fill="none" stroke="#b9b9b9" stroke-width="5" stroke-dasharray="3.2 3.1"/><circle cx="12" cy="12" r="6" fill="#b9b9b9"/><circle cx="12" cy="12" r="3" fill="#f7f7f7"/></svg>
  </nav>
</section>

<section class="screen screen--feature" aria-label="Recipe feature screen">
  <div class="feature-photo" role="img" aria-label="Photo of a wooden board with dried mango, dates, limes, nuts and grains on white wood"></div>
  <div class="feature-shade"></div>
  <p class="feature-kicker">Verdant Ledger</p>
  <h2 class="feature-title">Mango Recipes&nbsp; –<br>Ultimate Exquisite<br>Fresh Tasty Food</h2>
  <span class="feature-button">RECIPES</span>
</section>

</body>
</html>
```